IV Nutritional Clinic Web Design

We are working with Velmo. They are an IV Nutritional Clinic and in need of a new website design.
Some sites to use for inspiration:
https://brantlowcare.example
https://www.zolvarihealth.example
https://www.quellspa.example
https://pimrolift.example
https://www.dorvak-well.example/pages/iv-therapy-west-hollywood
https://www.tqoncowell.example/cancer-care/iv-drips/
https://drelmavita.example
https://salbrikmed.example
Thank you for taking the time to consider designing a website for us. We are web developers based in Stockton, CA, USA. Most of our projects go through the same process. Understanding this process may help you win a project with us. We custom-code all of our websites in-house. We don’t have any requirements as to what tools you use for your design, but we prefer Figma files. For any design that we label as four-stars, we send it to the client for review. The client picks the final design they want us to use. Once we complete this process, we will continue to show additional clients all the four-star sites and purchase them later. Your designs will have multiple chances to sell. For better chances of success, we ask that you follow these guidelines.
IMAGES:
If you use any images or icons in the design, we ask that you have a link to the asset so we can purchase the image/icon. Most of the designs we submit do not have the customer’s images on them unless they have some great images. Be creative; show us the feeling you are trying to portray with your image choices. Use any royalty-free site you choose. We subscribe to Corvix and mainly use their images, but we can purchase images outside of Corvix.
PLEASE NOTE: we will not submit designs to clients with watermarks on the images.
FONTS:
We ask that you identify the fonts used in the design. This can be done in a message if you want. We typically use Lumen Typeset and Corvix Fonts.
CONTENT:
We're always open to different content and ideas. We often submit designs with stock images so the client can see our vision. We typically take pictures after the website launch to use their images with our vision. Lorem Ipsum is fine for paragraphs, but we ask that you write the headers in correct English. We want to be able to show the vision and identify the sections of the website.
INSPIRATION:
We typically add a couple of links in the brief of websites we like to help you get started in your design.
REVISIONS:
We do not often ask for revisions of the designs unless we see something in the design that may not appeal to the client. If there are slight changes that we want to make, we do that in the development process.
FEEDBACK:
We rarely give feedback on designs during the design process. We are working on many website projects and do not have the time to provide feedback. We usually respond if your request is well thought out and asks specific questions, but a note asking “feedback, please” usually goes unanswered.
Number of Pages Required
1 page
Look and feel
Each slider illustrates characteristics of the customer's brand and the style your logo design should communicate.

```html
<!DOCTYPE html>
<html lang="en">
<head>
<meta charset="utf-8">
<title>Velmo Hydration — IV Nutritional Therapy</title>
<link href="https://fonts.googleapis.com/css2?family=Playfair+Display:wght@500;600;700&family=Albert+Sans:wght@400;500;600;700&display=swap" rel="stylesheet">
<style>
:root{
  --navy:#1d2b8f;
  --green:#7aa33a;
  --green-light:#eefbd9;
  --ink:#2a2a2a;
  --gray-bg:#eef0f3;
  --icon-bg:#dfe7fb;
  --white:#fff;
  --black:#0d0d0d;
}
*{box-sizing:border-box;margin:0;padding:0}
html,body{width:1200px;height:4405px;overflow:hidden}
body{position:relative;font-family:"Albert Sans",Arial,sans-serif;color:var(--ink);background:var(--white)}
.abs{position:absolute}
.serif{font-family:"Playfair Display",Georgia,serif}
.btn{position:absolute;background:var(--green);color:#fff;font-weight:600;font-size:12px;letter-spacing:.3px;display:flex;align-items:center;justify-content:center;text-transform:uppercase}
.tag{position:absolute;background:var(--navy);color:#fff;font-size:9.5px;letter-spacing:4px;font-weight:600;padding:3px 12px 3px 14px;text-transform:uppercase}
.tag::after{content:"";position:absolute;right:-22px;top:6px;width:16px;height:5px;background:var(--navy);border-radius:1px}
.section-title{position:absolute;left:0;width:1200px;text-align:center;font-family:"Playfair Display",Georgia,serif;font-size:25px;font-weight:600;color:#2d2d2d}
.photo{position:absolute;overflow:hidden}
.hero{left:0;top:0;width:1200px;height:711px;background:linear-gradient(100deg,#9fbdc3 0%,#b7ced1 40%,#c9d7d9 60%,#a9b5bd 100%)}
.hero-scene{left:560px;top:70px;width:640px;height:641px;background:radial-gradient(ellipse at 55% 45%,#8f6a4e 0%,#7b5f4c 30%,rgba(60,75,110,.7) 55%,rgba(160,180,190,0) 75%)}
.nav{left:115px;top:22px;width:723px;height:58px;background:#fff;display:flex;align-items:center}
.wordmark{font-family:"Albert Sans",Arial,sans-serif;font-weight:600;color:var(--navy);display:flex;align-items:center;gap:8px}
.wordmark .dot{width:10px;height:10px;background:var(--navy)}
.nav .wordmark{position:absolute;left:14px;font-size:26px}
.nav-links{position:absolute;left:246px;display:flex;gap:36px;font-size:11.5px;font-weight:500;color:#444}
.nav-links .on{color:var(--navy);font-weight:700;position:relative}
.nav-links .on::after{content:"";position:absolute;left:50%;top:20px;width:3px;height:10px;background:var(--navy)}
.hero h1{left:115px;top:218px;font-size:45px;line-height:58px;font-weight:600;color:var(--navy)}
.hero p{left:116px;top:408px;width:380px;color:#fff;font-size:12px;line-height:22px}
.hero .dots{left:56px;top:346px}
.about-copy{left:612px;width:460px;font-size:12px;line-height:22.5px;color:#444}
.services{left:0;top:1376px;width:1200px;height:856px;background:var(--gray-bg)}
.card{position:absolute;overflow:hidden;color:#fff}
.card span{position:absolute;left:0;right:0;bottom:22px;text-align:center;font-weight:600;font-size:17px}
.card.wellness{background:var(--navy)}
.card.wellness .frame{position:absolute;left:14px;top:14px;right:14px;bottom:14px;border:1px solid rgba(255,255,255,.6)}
.benefit{position:absolute;width:260px;font-size:11px;line-height:20px;color:#555}
.benefit b{display:block;font-size:13.5px;color:#222;font-weight:600;margin-bottom:2px}
.benefit.l{text-align:right}
.ico{position:absolute;width:64px;height:64px;border-radius:12px;background:var(--icon-bg);display:flex;align-items:center;justify-content:center}
.testi{left:0;top:2828px;width:1200px;height:624px;background:var(--green-light)}
.quote{left:692px;top:3093px;width:380px;font-size:14px;line-height:28.5px;color:#333}
.post-date{position:absolute;background:var(--navy);color:#fff;font-size:10.5px;padding:3px 8px}
.post-title{position:absolute;width:300px;font-size:17px;line-height:26px;color:#333}
.post-line{position:absolute;width:308px;height:1px;background:#e2e2e2}
.read{position:absolute;font-size:10px;letter-spacing:2.5px;color:#555}
.footer{left:0;top:3991px;width:1200px;height:414px;background:var(--black);color:#fff}
.fcol-title{position:absolute;font-size:13px;font-weight:700;letter-spacing:.5px}
.fdiv{position:absolute;width:2px;height:22px;background:var(--green)}
.flist{position:absolute;list-style:none;font-size:12px;color:#cfcfcf}
.flist li{height:28px}
.flist.small{font-size:11px}
</style>
</head>
<body>

<section class="abs hero">
  <div class="abs hero-scene" role="img" aria-label="Woman relaxing in a brown clinic recliner receiving an IV drip"></div>
  <nav class="abs nav">
    <div class="wordmark">Velmo<span class="dot"></span></div>
    <div class="nav-links"><span class="on">HOME</span><span>ABOUT</span><span>SERVICES</span><span>BENEFITS</span><span>BLOG</span><span>CONTACT</span></div>
  </nav>
  <div class="btn" style="left:865px;top:22px;width:219px;height:58px;font-size:12.5px">
    <svg width="22" height="20" viewBox="0 0 22 20" style="margin-right:12px"><rect x="1" y="3" width="18" height="15" rx="2" fill="none" stroke="#fff" stroke-width="1.5"/><line x1="1" y1="8" x2="19" y2="8" stroke="#fff" stroke-width="1.5"/><line x1="6" y1="1" x2="6" y2="5" stroke="#fff" stroke-width="1.5"/><line x1="14" y1="1" x2="14" y2="5" stroke="#fff" stroke-width="1.5"/></svg>
    Book Appointment
  </div>
  <svg class="abs dots" width="20" height="80" viewBox="0 0 20 80"><circle cx="8" cy="4" r="1.5" fill="#fff"/><circle cx="8" cy="34" r="7" fill="none" stroke="var(--navy)" stroke-width="1.5"/><circle cx="8" cy="34" r="3" fill="var(--navy)"/><circle cx="8" cy="68" r="1.5" fill="#fff"/></svg>
  <h1 class="abs serif">Revitalize Your Body<br>With Customized<br>Velmo Hydration.</h1>
  <p class="abs">Our specialized IV and injection nutrient therapies deliver essential vitamins, minerals, and amino acids to support your body's optimal function.</p>
  <div class="btn" style="left:115px;top:506px;width:198px;height:41px">Book An Appointment</div>
  <svg class="abs" style="left:313px;top:515px" width="40" height="22" viewBox="0 0 40 22"><rect x="0" y="6" width="22" height="10" fill="var(--green)"/><rect x="22" y="2" width="4" height="18" fill="var(--green)"/><rect x="26" y="9" width="12" height="4" fill="var(--green)"/></svg>
</section>

<div class="photo" style="left:123px;top:779px;width:441px;height:294px;border-radius:14px;background:linear-gradient(120deg,#d9d4c8,#9fb9c9 45%,#2b3f64 80%)" role="img" aria-label="Nurse attending a smiling senior patient in a green infusion chair"></div>
<div class="photo" style="left:125px;top:1095px;width:217px;height:200px;border-radius:8px;background:linear-gradient(135deg,#e7ecec,#9ccc3b 55%,#c7d0d0)" role="img" aria-label="Lime green infusion chair in a bright clinic room"></div>
<div class="photo" style="left:371px;top:1095px;width:181px;height:200px;border-radius:8px;background:linear-gradient(160deg,#efe9e6,#e7b4a6 50%,#c9cfd9)" role="img" aria-label="Gloved hand holding an IV bag filled with sliced fruits"></div>
<div class="tag" style="left:612px;top:795px">About Us</div>
<h2 class="abs serif" style="left:612px;top:826px;font-size:25px;font-weight:600;color:#2d2d2d">Welcome to Velmo Hydration</h2>
<p class="abs about-copy" style="top:875px">Velmo Hydration was established by a board-certified medical professional. We successfully integrate cutting-edge medical research with personalized IV nutritional therapy to provide our clients with the most effective and efficient treatment options.</p>
<p class="abs about-copy" style="top:985px">Gone are the days of relying solely on traditional medicine to address nutritional deficiencies and health concerns. At Velmo Hydration, we offer a unique and innovative approach to wellness, providing customized IV nutritional therapies in a relaxing and welcoming environment.</p>
<p class="abs about-copy" style="top:1097px">Whether you're seeking relief from chronic fatigue, migraines, or digestive issues, or simply looking to boost your energy and immune system, our IV nutritional therapies can help. Our experienced medical team will work closely with you to create a personalized treatment plan tailored to your specific needs and health goals.</p>
<div class="btn" style="left:613px;top:1236px;width:197px;height:39px">Book An Appointment</div>

<section class="abs services"></section>
<div class="tag" style="left:523px;top:1426px">Our Services</div>
<h2 class="section-title" style="top:1456px">IV Treatment Programs</h2>
<div class="card" style="left:116px;top:1526px;width:308px;height:274px;background:linear-gradient(180deg,#c8611f,#8a3a18 55%,#1d1410)" role="img" aria-label="Silhouette of a man flexing at sunset"><span>Energy Boost IV</span></div>
<div class="card wellness" style="left:446px;top:1526px;width:306px;height:274px"><div class="frame"></div>
  <svg style="position:absolute;left:108px;top:50px" width="90" height="90" viewBox="0 0 90 90" fill="none" stroke="#fff" stroke-width="3"><circle cx="45" cy="18" r="10"/><path d="M45 30c-10 0-16 8-16 18l-14 14M45 30c10 0 16 8 16 18l14 14M29 48c0 12 16 22 16 22s16-10 16-22M14 72h62"/></svg>
  <div style="position:absolute;top:164px;left:0;right:0;text-align:center;font-weight:600;font-size:17px">Wellness IV</div>
  <svg style="position:absolute;left:136px;top:204px" width="34" height="34" viewBox="0 0 34 34"><circle cx="17" cy="17" r="16" fill="#fff"/><path d="M11 17h12M19 13l4 4-4 4" stroke="var(--navy)" stroke-width="1.6" fill="none"/></svg>
</div>
<div class="card" style="left:774px;top:1526px;width:308px;height:274px;background:linear-gradient(160deg,#f0b23a,#e38a1e 50%,#5c3a1d)" role="img" aria-label="Halved oranges on a wooden board"><span>Immunity IV</span></div>
<div class="card" style="left:116px;top:1825px;width:308px;height:275px;background:linear-gradient(90deg,#9a8274,#c9b3a2 50%,#b9b3ad)" role="img" aria-label="Split portrait comparing younger and older skin"><span>Anti-Aging IV</span></div>
<div class="card" style="left:446px;top:1825px;width:306px;height:275px;background:linear-gradient(180deg,#d7dce4,#efe9e3 50%,#c3b7ad)" role="img" aria-label="Woman measuring her waist with a tape"><span>Weight Management IV</span></div>
<div class="card" style="left:774px;top:1825px;width:308px;height:275px;background:radial-gradient(circle at 45% 40%,#e0457c,#6a2a7a 40%,#0c2a4a 75%)" role="img" aria-label="Glowing illustration of a human brain"><span>Brain Improvement IV</span></div>
<div class="btn" style="left:502px;top:2141px;width:195px;height:42px">View All Services</div>

<div class="tag" style="left:537px;top:2277px">Benefits</div>
<h2 class="section-title" style="top:2307px">Discover the Power of IV Nutrition</h2>
<svg class="abs" style="left:430px;top:2405px" width="336" height="430" viewBox="0 0 336 430">
  <line x1="168" y1="0" x2="168" y2="430" stroke="#e3e6ee" stroke-width="3"/>
  <circle cx="168" cy="172" r="164" fill="#eef1fb" stroke="#e3e6ee" stroke-width="2"/>
  <circle cx="168" cy="172" r="146" fill="#fff"/>
</svg>
<div class="abs wordmark" style="left:500px;top:2548px;width:196px;justify-content:center;font-size:46px">Velmo</div>
<div class="benefit l" style="left:62px;top:2417px"><b>Rapid Hydration</b>Replenish essential fluids and electrolytes to combat dehydration</div>
<div class="ico" style="left:341px;top:2418px"><svg width="34" height="34" viewBox="0 0 34 34" fill="none" stroke="var(--navy)" stroke-width="2"><circle cx="17" cy="18" r="12"/><path d="M17 11c-3 4-4 6-4 8a4 4 0 008 0c0-2-1-4-4-8z"/></svg></div>
<div class="benefit l" style="left:62px;top:2539px"><b>Enhances Immune Function</b>IV vitamins and minerals support immune system function.</div>
<div class="ico" style="left:341px;top:2540px"><svg width="34" height="34" viewBox="0 0 34 34" fill="none" stroke="var(--navy)" stroke-width="2"><path d="M17 4l11 4v9c0 7-5 11-11 13C11 28 6 24 6 17V8z"/><circle cx="17" cy="17" r="4"/></svg></div>
<div class="benefit l" style="left:62px;top:2669px"><b>Reduced Stress and Anxiety</b>Find calm and relaxation with specially formulated infusions promoting</div>
<div class="ico" style="left:341px;top:2670px"><svg width="34" height="34" viewBox="0 0 34 34" fill="none" stroke="var(--navy)" stroke-width="2"><circle cx="15" cy="19" r="11"/><path d="M10 22c3 3 7 3 10 0M10 16h2M18 16h2"/><circle cx="27" cy="8" r="4"/></svg></div>
<div class="ico" style="left:800px;top:2418px"><svg width="34" height="34" viewBox="0 0 34 34" fill="none" stroke="var(--navy)" stroke-width="2"><path d="M28 14A12 12 0 006 12M6 20a12 12 0 0022 2"/><path d="M18 9l-5 9h6l-3 8"/></svg></div>
<div class="benefit" style="left:882px;top:2417px"><b>Boosts Energy</b>IV nutrients help increase energy levels and reduce fatigue.</div>
<div class="ico" style="left:800px;top:2540px"><svg width="36" height="34" viewBox="0 0 36 34" fill="none" stroke="var(--navy)" stroke-width="2"><circle cx="22" cy="6" r="3"/><path d="M12 14l6-4 5 5-4 6 5 5M18 21l-6 6M23 15l6 1M4 12h6M2 18h6M4 24h5"/></svg></div>
<div class="benefit" style="left:882px;top:2539px"><b>Improved Athletic Performance</b>Optimize physical performance with tailored amino acid infusions and</div>
<div class="ico" style="left:800px;top:2670px"><svg width="34" height="34" viewBox="0 0 34 34" fill="none" stroke="var(--navy)" stroke-width="2"><circle cx="17" cy="8" r="4"/><path d="M17 13c-5 0-7 4-7 9l-5 5M17 13c5 0 7 4 7 9l5 5M10 22c0 4 7 7 7 7s7-3 7-7M5 30h24"/></svg></div>
<div class="benefit" style="left:882px;top:2669px"><b>Personalized Wellness</b>Receive customized treatment plans tailored to address specific health</div>

<section class="abs testi"></section>
<div class="tag" style="left:522px;top:2872px">Testimonials</div>
<h2 class="section-title" style="top:2902px">What Our Customers Says About Us</h2>
<div class="photo" style="left:115px;top:2981px;width:386px;height:386px;border-radius:50%;background:linear-gradient(130deg,#d9dde0,#b7a79a 45%,#7a1f2a 65%,#cfd4d6)" role="img" aria-label="Woman receiving an IV infusion in a clinic chair"></div>
<div class="photo" style="left:393px;top:3126px;width:232px;height:232px;border-radius:50%;border:3px solid #fff;background:radial-gradient(circle at 50% 55%,#f3e25a,#cfd8e6 40%,#7b9ac0 80%)" role="img" aria-label="IV bag labelled high-dose vitamin C with a lemon slice"></div>
<div class="abs serif" style="left:462px;top:2950px;font-size:190px;line-height:1;color:var(--green);font-weight:700">&ldquo;</div>
<div class="photo" style="left:692px;top:3010px;width:46px;height:46px;border-radius:50%;background:linear-gradient(#cfe3f0,#8aa6bd)" role="img" aria-label="Customer avatar"></div>
<div class="photo" style="left:762px;top:3005px;width:58px;height:58px;border-radius:50%;border:3px solid var(--green);background:linear-gradient(#c73a2f,#6e1d1a)" role="img" aria-label="Reviewer avatar"></div>
<div class="photo" style="left:842px;top:3010px;width:46px;height:46px;border-radius:50%;background:linear-gradient(#b38a6d,#4f3326)" role="img" aria-label="Customer avatar"></div>
<p class="abs quote">“I was skeptical at first, but after one session, I felt like a new person! My energy levels skyrocketed and I felt refreshed and rejuvenated. I noticed a significant improvement in my mental clarity, and I was able to focus and concentrate better. My stress and anxiety levels decreased, and I felt a sense of calm and relaxation that I hadn't experienced in a long time.”</p>
<div class="abs" style="left:693px;top:3318px;font-size:16px;color:#222">Mirela Dostane</div>
<div class="abs" style="left:693px;top:3342px;font-size:13px;color:#555">Founder</div>
<svg class="abs" style="left:944px;top:3322px" width="90" height="34" viewBox="0 0 90 34"><circle cx="17" cy="17" r="15" fill="none" stroke="var(--navy)" stroke-width="1.5"/><path d="M23 17H11M15 13l-4 4 4 4" stroke="var(--navy)" stroke-width="1.5" fill="none"/><circle cx="62" cy="17" r="15" fill="none" stroke="var(--green)" stroke-width="1.5"/><path d="M56 17h12M64 13l4 4-4 4" stroke="var(--green)" stroke-width="1.5" fill="none"/></svg>

<div class="tag" style="left:522px;top:3492px">Latest Blogs</div>
<h2 class="section-title" style="top:3528px">Check Out Our Daily Articles</h2>
<div class="photo" style="left:116px;top:3594px;width:308px;height:195px;background:linear-gradient(180deg,#f3a81f,#f7d97a 45%,#eceff2)" role="img" aria-label="Orange IV bag with drip line"></div>
<div class="photo" style="left:446px;top:3594px;width:308px;height:195px;background:linear-gradient(135deg,#dfe7ee,#3f63b8 45%,#f2b35b 60%,#e7ecf0)" role="img" aria-label="Gloved hand holding a fruit-filled IV bag"></div>
<div class="photo" style="left:776px;top:3594px;width:308px;height:195px;background:linear-gradient(135deg,#c7cfd8,#8a6f5d 45%,#4d6fa6 70%,#dfe5ea)" role="img" aria-label="Nurse preparing an IV line for a patient"></div>
<div class="post-date" style="left:116px;top:3804px">January 01</div>
<div class="post-date" style="left:446px;top:3804px;background:var(--green)">January 05</div>
<div class="post-date" style="left:776px;top:3804px">January 10</div>
<div class="post-title" style="left:116px;top:3837px">Revitalize Your Health: The Power of IV Nutritional Therapy</div>
<div class="post-title" style="left:446px;top:3837px">Drip, Recharge, Repeat: The Benefits of IV Nutrition</div>
<div class="post-title" style="left:776px;top:3837px">The IV Advantage: How Nutritional Therapy Can Transform Your Health</div>
<div class="post-line" style="left:116px;top:3902px"></div>
<div class="post-line" style="left:446px;top:3902px"></div>
<div class="post-line" style="left:776px;top:3902px"></div>
<div class="read" style="left:116px;top:3920px">READ MORE</div>
<div class="read" style="left:446px;top:3920px;color:var(--green)">READ MORE ▸</div>
<div class="read" style="left:776px;top:3920px">READ MORE</div>

<footer class="abs footer">
  <div class="abs wordmark" style="left:116px;top:64px;font-size:36px">Velmo</div>
  <div class="abs" style="left:150px;top:134px;display:flex;gap:12px">
    <span style="width:18px;height:18px;border:1.5px solid #fff;border-radius:3px"></span>
    <span style="width:18px;height:18px;border:1.5px solid #fff;border-radius:3px"></span>
    <span style="width:18px;height:18px;border:1.5px solid #fff;border-radius:3px"></span>
  </div>
  <div class="fdiv" style="left:330px;top:64px"></div>
  <div class="fcol-title" style="left:366px;top:68px">NAVIGATION</div>
  <ul class="flist" style="left:366px;top:105px"><li>Home</li><li>About us</li><li>Services</li><li>Benefits</li><li>Blog</li><li>Contact Us</li></ul>
  <div class="fdiv" style="left:555px;top:64px"></div>
  <div class="fcol-title" style="left:595px;top:68px">THERAPEUTIC SERVICES</div>
  <ul class="flist small" style="left:598px;top:105px"><li>IV Antibiotics</li><li>Nutrition Support</li><li>Immunoglobulin</li><li>Chronic Inflammatory Disorders</li><li>Neurological Disorders</li><li>Bleeding Disorders</li><li>Women's Health</li><li>Heart Failure</li><li>Specialized Therapies</li></ul>
  <div class="fdiv" style="left:848px;top:64px"></div>
  <div class="fcol-title" style="left:881px;top:68px">CONTACT US</div>
  <svg class="abs" style="left:880px;top:110px" width="18" height="20" viewBox="0 0 18 20" fill="none" stroke="#fff" stroke-width="1.5"><path d="M9 19s7-6 7-11A7 7 0 002 8c0 5 7 11 7 11z"/><circle cx="9" cy="8" r="2.5"/></svg>
  <div class="abs" style="left:918px;top:109px;font-size:11.5px;line-height:22px;color:#ddd">48 Larkspur Avenue, 210<br>Fairhaven, USA</div>
  <svg class="abs" style="left:880px;top:170px" width="18" height="18" viewBox="0 0 18 18" fill="none" stroke="#fff" stroke-width="1.5"><path d="M3 1h4l2 5-3 2a11 11 0 005 5l2-3 5 2v4a2 2 0 01-2 2C8 18 0 10 1 3a2 2 0 012-2z"/></svg>
  <div class="abs" style="left:918px;top:172px;font-size:11.5px;color:#ddd">555 204 7781</div>
  <svg class="abs" style="left:880px;top:213px" width="18" height="14" viewBox="0 0 18 14" fill="none" stroke="#fff" stroke-width="1.5"><rect x="1" y="1" width="16" height="12" rx="1"/><path d="M1 2l8 6 8-6"/></svg>
  <div class="abs" style="left:918px;top:212px;font-size:11.5px;color:#ddd">Contact@velmo.example</div>
  <div class="abs" style="left:0;top:385px;width:1200px;text-align:center;font-size:9.5px;color:#777">© 2025 Velmo Hydration | All Rights Reserved.</div>
</footer>

</body>
</html>
```